Business branding (card, web design) needed for Remedial / Sports massage

I need a clean, fresh design for my sports massage business called Swiftmoor-Core.

I work with high profile professional sports teams (massage, clinical tapeing, health assessments, pilates, coaching) however would like to expand into the entertainment market so need a design that would appeal to both.
NO LOTUS FLOWERS, HANDS OR YOGA POSES FOR DESIGNS

The successful brand design will need to be scalable (e.g. resolution/sizing) to work holistically across my website, marketing collateral and clothing.

Colour pallets that appeal to me - Black, white, blue, green, taupe,
and would prefer clean crisp designs that evoke professionalism, continuous improvement, flow and balance.

Good Luck, can't wait to find my new brand... :)
Updates

I have uploaded a business card that I do like,  See if you can be creative with the logo

Thanks

Target Market(s)

professional sports teams / athletes, and entertainment professionals.

I HAVE UPLOADED A PDF OF WHAT I HAVE DONE. YOU MAY USE LOGO BUT BE CREATIVE PLEASE.

Industry/Entity Type

Entertainment

Contact Information for Business Card

Swiftmoor-Core
'Move Stronger' (strap line)

Carla Wendover
Director / Remedial Massage

0471382605
612 Brisley Street
Larkfield, VIC 3271

www.swiftmoor-core.com.au
info@swiftmoor-core.com.au

Logo Text

Swiftmoor-Core

Logo styles of interest
Pictorial/Combination Logo
Abstract Logo
Requirements
Should not have
• FLOWERS

```html
<!DOCTYPE html>
<html lang="en">
<head>
<meta charset="utf-8">
<title>Swiftmoor-Core Business Card</title>
<link rel="stylesheet" href="https://fonts.googleapis.com/css2?family=Didact+Gothic&display=swap">
<style>
  :root {
    --stage: #3b3c3e;
    --teal: #2cb1c1;
    --green: #8cc63f;
    --white: #ffffff;
    --ink-light: #ffffff;
  }
  * { box-sizing: border-box; margin: 0; padding: 0; }
  html, body {
    width: 1200px; height: 800px; overflow: hidden;
    background: var(--stage);
    font-family: "Didact Gothic", sans-serif;
  }
  .stage { position: relative; width: 1200px; height: 800px; }
  .card {
    position: absolute; top: 234px;
    width: 510px; height: 296px;
    border-radius: 24px; overflow: hidden;
  }
  /* front */
  .card-front { left: 70px; background: var(--white); }
  .brand {
    position: absolute; left: 0; right: 0; top: 40px;
    display: flex; flex-direction: column; align-items: center;
  }
  .brand-row { display: flex; align-items: center; gap: 10px; }
  .brand-dot { width: 18px; height: 18px; border-radius: 50%; background: var(--green); }
  .brand-name { font-size: 36px; color: var(--teal); letter-spacing: 0.5px; }
  .tagline { margin-top: 4px; font-size: 15px; color: var(--teal); }
  .band {
    position: absolute; left: 0; right: 0; top: 146px; height: 100px;
    background: var(--teal); color: var(--ink-light);
  }
  .person { position: absolute; left: 56px; top: 32px; }
  .person-name { font-size: 24px; line-height: 1.1; }
  .person-role { font-size: 12px; margin-top: 4px; }
  .contact { position: absolute; left: 318px; top: 14px; font-size: 13.5px; line-height: 1.35; }
  .contact-line { display: flex; align-items: flex-start; gap: 8px; }
  .contact-line + .contact-line { margin-top: 10px; }
  .contact-line svg { flex: none; width: 18px; height: 18px; margin-top: 1px; }
  /* back */
  .card-back { left: 624px; background: var(--teal); }
  .back-panel {
    position: absolute; left: 46px; top: 36px; width: 420px; height: 212px;
    background: var(--white); border-radius: 22px;
  }
  .back-links {
    position: absolute; left: 56px; right: 24px; top: 256px;
    display: flex; gap: 30px; color: var(--ink-light); font-size: 14px;
  }
  .back-link { display: flex; align-items: center; gap: 8px; }
  .back-link svg { width: 18px; height: 18px; flex: none; }
</style>
</head>
<body>
<main class="stage">
  <section class="card card-front" aria-label="Business card front">
    <div class="brand">
      <div class="brand-row">
        <span class="brand-dot"></span>
        <span class="brand-name">Swiftmoor-Core</span>
      </div>
      <span class="tagline">'Move Stronger'</span>
    </div>
    <div class="band">
      <div class="person">
        <p class="person-name">Carla Wendover</p>
        <p class="person-role">Director / Remedial Massage</p>
      </div>
      <div class="contact">
        <div class="contact-line">
          <svg viewBox="0 0 20 20" aria-hidden="true">
            <path d="M2 10 L10 3 L18 10" fill="none" stroke="#fff" stroke-width="2"/>
            <path d="M5 9 V17 H9 V12 H11 V17 H15 V9" fill="none" stroke="#fff" stroke-width="2"/>
          </svg>
          <span>612 Brisley Street<br>Larkfield<br>Vic 3271</span>
        </div>
        <div class="contact-line">
          <svg viewBox="0 0 20 20" aria-hidden="true">
            <rect x="5" y="1.5" width="10" height="17" rx="2" fill="#fff"/>
            <rect x="7" y="4" width="6" height="9" fill="var(--teal)"/>
            <circle cx="10" cy="15.5" r="1" fill="var(--teal)"/>
          </svg>
          <span>0471382605</span>
        </div>
      </div>
    </div>
  </section>

  <section class="card card-back" aria-label="Business card back">
    <div class="back-panel"></div>
    <div class="back-links">
      <span class="back-link">
        <svg viewBox="0 0 20 20" aria-hidden="true">
          <circle cx="10" cy="10" r="8" fill="none" stroke="#fff" stroke-width="1.8"/>
          <ellipse cx="10" cy="10" rx="3.5" ry="8" fill="none" stroke="#fff" stroke-width="1.5"/>
          <line x1="2" y1="10" x2="18" y2="10" stroke="#fff" stroke-width="1.5"/>
        </svg>
        www.swiftmoor-core.com.au
      </span>
      <span class="back-link">
        <svg viewBox="0 0 20 20" aria-hidden="true">
          <rect x="2" y="4.5" width="16" height="11" fill="none" stroke="#fff" stroke-width="1.8"/>
          <path d="M2 4.5 L10 11 L18 4.5" fill="none" stroke="#fff" stroke-width="1.8"/>
        </svg>
        info@swiftmoor-core.com.au
      </span>
    </div>
  </section>
</main>
</body>
</html>
```